Business Card Design for Pastor/Church Leadership - simple, elegant, "different"

Design a name card based on logo and color from our branding guide - see file "MBF Logo and Color".
The teal frame around the logo is not part of the logo and is a not necessary design element for the name card (as the attached PDF file may suggest).
The font suggested by branding is "Frutiger 55 Roman".
The file "not good.pdf", a sample of a name card that is NOT good.
- fonts too small to read
- the tagline on the logo "Still waters, open door" not easy to read with logo used in this design
- "MAPLE GROVE FELLOWSHIP" unnecessarily duplicated - possibly because logo too small
- not sure about the green frame, probably better to drop

Target Market(s)

broad, all people the pastor of an international church in Tokyo meets

Industry/Entity Type

Business

Contact Information for Business Card

Mattias R. Pellworth
Pastor
3-9-4 Kawaranodai, Shibuya-ku
Tokyo 158-0093 (Church)
2-21 Ochibamachi, Shibuya-ku
Tokyo 158-0097 (Home)
Tel: 03-5817-2963
E-mail: pastor@maplegrovefell.org
URL: http://www.maplegrovefell.org

Font styles to use
Sans Serif
Other font styles liked:
• Frutiger 55 Roman (want, not must)

Requirements
Must have
• must include logo
• must make use of the "bright turquoise color"
• Cyan = 59, Magenta = 0, Yellow=24, Black=0
• Red=3.1%, Green=91%, Blue=87.1%
• Key Info (name) must be easy to read (see notes on bad sample namecard attached)

```html
<!DOCTYPE html>
<html lang="en">
<head>
<meta charset="utf-8">
<title>Maple Grove Fellowship – Business Card</title>
<link href="https://fonts.googleapis.com/css2?family=Source+Sans+3:wght@400;600&display=swap" rel="stylesheet">
<style>
  :root {
    --stage: #3b3431;
    --card: #0b0b0b;
    --teal: #5cc8cc;
    --ink: #e4e4e4;
    --muted: #bdbdbd;
    --silver: #c9c9c9;
    --silver-dim: #9a9a9a;
    --divider: #2d5f61;
  }
  * { margin: 0; padding: 0; box-sizing: border-box; }
  html, body { width: 1200px; height: 900px; overflow: hidden; }
  body {
    background: var(--stage);
    font-family: "Source Sans 3", "Frutiger", Arial, sans-serif;
    position: relative;
  }
  .card {
    position: absolute;
    top: 300px;
    width: 520px;
    height: 300px;
    background: var(--card);
    box-shadow: 0 10px 30px rgba(0,0,0,.45);
  }
  .card--front { left: 50px; }
  .card--back { left: 630px; }

  /* front */
  .front__mark {
    position: absolute;
    left: 40px;
    bottom: 46px;
    color: var(--teal);
    font-weight: 600;
    font-size: 64px;
    letter-spacing: 1px;
    line-height: 1;
  }
  .front__divider {
    position: absolute;
    left: 232px;
    top: 108px;
    width: 1px;
    height: 130px;
    background: var(--divider);
  }
  .front__info {
    position: absolute;
    left: 262px;
    top: 40px;
    right: 20px;
    color: var(--ink);
    font-size: 14px;
    line-height: 1.3;
  }
  .name { color: var(--teal); font-size: 21px; font-weight: 400; line-height: 1.15; }
  .role { font-size: 12.5px; color: var(--muted); margin-bottom: 14px; }
  .contact { list-style: none; margin-bottom: 12px; }
  .contact li { display: flex; align-items: center; gap: 6px; font-size: 13.5px; }
  .contact svg { width: 10px; height: 10px; flex: none; }
  .label { color: var(--teal); font-size: 15px; }
  .address { margin-bottom: 8px; }

  /* back */
  .back__brand {
    position: absolute;
    left: 0; right: 0;
    top: 60px;
    text-align: center;
  }
  .back__mark {
    color: var(--silver);
    font-weight: 600;
    font-size: 56px;
    letter-spacing: 2px;
    line-height: 1;
    margin-bottom: 26px;
  }
  .back__name {
    color: var(--silver);
    font-size: 17px;
    letter-spacing: 2.5px;
    display: inline-block;
    padding: 0 4px 8px;
    border-bottom: 1px solid var(--silver-dim);
  }
  .back__tagline {
    color: var(--silver-dim);
    font-size: 16px;
    letter-spacing: 1px;
    margin-top: 8px;
  }
</style>
</head>
<body>
  <section class="card card--front">
    <div class="front__mark">MBF</div>
    <div class="front__divider"></div>
    <div class="front__info">
      <h1 class="name">Mattias R. Pellworth</h1>
      <p class="role">Pastor</p>
      <ul class="contact">
        <li>
          <svg viewBox="0 0 10 10" aria-hidden="true"><path fill="#5cc8cc" d="M2 0.5 L3.6 2.8 L2.7 3.8 Q3.6 5.8 6.2 7.3 L7.2 6.4 L9.5 8 L8.3 9.5 Q1 8.5 0.5 1.7 Z"/></svg>
          03-5817-2963
        </li>
        <li>
          <svg viewBox="0 0 10 10" aria-hidden="true"><rect x="0.5" y="2" width="9" height="6.5" fill="#5cc8cc"/><path d="M0.8 2.3 L5 5.6 L9.2 2.3" fill="none" stroke="#0b0b0b" stroke-width="0.9"/></svg>
          pastor@maplegrovefell.org
        </li>
        <li>
          <svg viewBox="0 0 10 10" aria-hidden="true"><circle cx="5" cy="5" r="4.5" fill="#5cc8cc"/><path d="M0.8 5 H9.2 M5 0.6 Q2.4 5 5 9.4 M5 0.6 Q7.6 5 5 9.4" fill="none" stroke="#0b0b0b" stroke-width="0.6"/></svg>
          www.maplegrovefell.org
        </li>
      </ul>
      <p class="label">Church Address</p>
      <p class="address">3-9-4 Kawaranodai, Shibuya-ku<br>Tokyo 158-0093</p>
      <p class="label">Home Address</p>
      <p class="address">2-21 Ochibamachi, Shibuya-ku<br>Tokyo 158-0097</p>
    </div>
  </section>

  <section class="card card--back">
    <div class="back__brand">
      <div class="back__mark">MBF</div>
      <div class="back__name">MAPLE GROVE FELLOWSHIP</div>
      <p class="back__tagline">Still waters, open door</p>
    </div>
  </section>
</body>
</html>
```